Contemporary Elegant Business Card Design for an International Trade Company in the Wine Industry

We need a new business card design for an international trade company in the wine and winemaking industry. The overall feel of the card should be contemporary, upscale, luxurious and elegant. It should communicate confidence and professionalism. The colors should complementary to our logo design (burgundy, gold, and black).
Inspiration: rich velvet tapestry
The card should include the following information:
Business: Brovenna Trading/Shipping, LLC.
Name: Marcus T. Hollenbrand
Title: CEO
Email: mark@brovennatrading.example
Phone: 555-294-6172
www.brovennatrading.example
Updates
Project Deadline Extended
Reason: We'd like the designers that we requested some additional designs from to still submit designs. Thank you!
Industry/Entity Type
Business
Contact Information for Business Card
Title: CEO
Phone: 555-294-6172
www.brovennatrading.example
Look and feel

```html
<!DOCTYPE html>
<html lang="en">
<head>
<meta charset="utf-8">
<title>Brovenna Trading/Shipping – Business Card</title>
<link rel="stylesheet" href="https://fonts.googleapis.com/css2?family=Red+Hat+Display:wght@400;500;600&display=swap">
<style>
  :root {
    --stage: #e6e7e8;
    --card: #ffffff;
    --band: #f8f8f8;
    --burgundy: #6b0f1a;
    --gold: #c8943a;
    --globe-light: #f3f3f3;
    --globe-mid: #ebebeb;
    --strip: #e9e9e9;
  }
  html, body {
    margin: 0;
    padding: 0;
    width: 1200px;
    height: 1000px;
    overflow: hidden;
    background: var(--stage);
    font-family: "Red Hat Display", Arial, sans-serif;
  }
  .stage { position: relative; width: 1200px; height: 1000px; }
  .card {
    position: absolute;
    width: 514px;
    height: 321px;
    background: var(--card);
    overflow: hidden;
  }
  .card--front { left: 166px; top: 124px; }
  .card--back { left: 520px; top: 550px; }
  .globe-art { position: absolute; inset: 0; }

  .front-band {
    position: absolute; left: 0; right: 0; top: 98px; height: 125px;
    background: var(--band); opacity: .92;
  }
  .front-lockup { position: absolute; left: 119px; top: 124px; display: flex; align-items: center; gap: 17px; }
  .brand-square {
    width: 70px; height: 70px; box-sizing: border-box;
    border: 1px solid var(--burgundy); padding: 3px;
  }
  .brand-square span { display: block; width: 100%; height: 100%; background: var(--burgundy); }
  .front-name {
    width: 184px; border-top: 1px solid var(--burgundy); border-bottom: 1px solid var(--burgundy);
    padding: 13px 0 14px; color: var(--burgundy); font-weight: 600;
  }
  .brand-name { display: block; font-size: 21px; line-height: 1.05; letter-spacing: .3px; }
  .brand-sub { display: block; font-size: 13.5px; line-height: 1.3; margin-top: 3px; }

  .back-lockup {
    position: absolute; left: 40px; top: 41px; width: 146px;
    text-align: center; color: var(--burgundy); font-weight: 600;
  }
  .back-lockup .brand-square { width: 66px; height: 66px; margin: 0 auto 7px; }
  .back-lockup .brand-name { font-size: 16px; }
  .back-lockup .brand-sub { font-size: 10px; margin-top: 1px; }

  .person { position: absolute; left: 227px; top: 156px; color: var(--burgundy); white-space: nowrap; }
  .person-name { font-size: 19px; font-weight: 600; letter-spacing: -.2px; }
  .person-title { font-size: 18px; font-weight: 400; margin-left: 6px; padding-left: 6px; border-left: 1px solid var(--burgundy); }

  .contact-list { position: absolute; left: 226px; top: 208px; margin: 0; padding: 0; list-style: none; }
  .contact-item { display: flex; align-items: center; height: 24px; color: var(--burgundy); font-size: 15px; }
  .contact-item svg { width: 18px; height: 18px; margin-right: 15px; flex: none; }
  .back-strip { position: absolute; left: 0; right: 0; top: 292px; height: 15px; background: var(--strip); }
</style>
</head>
<body>
<div class="stage">

  <section class="card card--front" aria-label="Business card front">
    <svg class="globe-art" viewBox="0 0 514 321" role="img" aria-label="Faint world globe map with latitude and longitude lines">
      <defs>
        <radialGradient id="globeFront" cx="0.5" cy="0.55" r="0.5">
          <stop offset="0" stop-color="#f2f2f2"/>
          <stop offset="1" stop-color="#f7f7f7"/>
        </radialGradient>
      </defs>
      <circle cx="256" cy="170" r="246" fill="url(#globeFront)"/>
    </svg>
    <div class="front-band"></div>
    <div class="front-lockup">
      <div class="brand-square"><span></span></div>
      <div class="front-name">
        <span class="brand-name">Brovenna</span>
        <span class="brand-sub">Trading/Shipping, LLC</span>
      </div>
    </div>
  </section>

  <section class="card card--back" aria-label="Business card back">
    <svg class="globe-art" viewBox="0 0 514 321" role="img" aria-label="Faint world globe map with latitude and longitude lines">
      <defs>
        <radialGradient id="globeBack" cx="0.5" cy="0.5" r="0.5">
          <stop offset="0" stop-color="#f0f0f0"/>
          <stop offset="1" stop-color="#f8f8f8"/>
        </radialGradient>
      </defs>
      <circle cx="510" cy="210" r="215" fill="url(#globeBack)"/>
    </svg>

    <div class="back-lockup">
      <div class="brand-square"><span></span></div>
      <span class="brand-name">Brovenna</span>
      <span class="brand-sub">Trading/Shipping, LLC</span>
    </div>

    <div class="person">
      <span class="person-name">Marcus T. Hollenbrand</span><span class="person-title">CEO</span>
    </div>

    <ul class="contact-list">
      <li class="contact-item">
        <svg viewBox="0 0 24 24" aria-hidden="true"><path fill="#6b0f1a" d="M6.6 10.8a15.5 15.5 0 0 0 6.6 6.6l2.2-2.2c.3-.3.7-.4 1-.2 1.1.4 2.3.6 3.6.6.6 0 1 .4 1 1V20c0 .6-.4 1-1 1A17 17 0 0 1 3 4c0-.6.4-1 1-1h3.5c.6 0 1 .4 1 1 0 1.3.2 2.5.6 3.6.1.3 0 .7-.2 1z"/></svg>
        555-294-6172
      </li>
      <li class="contact-item">
        <svg viewBox="0 0 24 24" aria-hidden="true"><rect x="3" y="6" width="18" height="12" rx="1" fill="#6b0f1a"/><path d="M3.5 6.5 12 13l8.5-6.5" fill="none" stroke="#fff" stroke-width="1.4"/></svg>
        mark@brovennatrading.example
      </li>
      <li class="contact-item">
        <svg viewBox="0 0 24 24" aria-hidden="true"><g fill="none" stroke="#6b0f1a" stroke-width="1.4"><circle cx="12" cy="12" r="8.5"/><ellipse cx="12" cy="12" rx="3.8" ry="8.5"/><path d="M3.5 12h17M5 7.5h14M5 16.5h14"/></g></svg>
        www.brovennatrading.example
      </li>
    </ul>

    <div class="back-strip"></div>
  </section>

</div>
</body>
</html>
```